Paperback book cover design front and back covers

The book is called "Pavement Endurance Blueprint: The Complete Handbook for Racing Your Longest Distance - Featuring Schedules, Wisdom and Target-Reaching Pointers "

It is a 6" x 9" book with 205 pages. This is an advanced book for runners who have been running and trying to hit their marathon goals, but haven't been able to do so. This needs to portray a professional coaching image and high performing athlete.

I have running photos of myself running marathons if you thought that was the route to take, but I'm open to your creative influence.

```html
<!DOCTYPE html>
<html lang="en">
<head>
<meta charset="utf-8">
<title>Pavement Endurance Blueprint – Paperback Cover</title>
<link rel="stylesheet" href="https://fonts.googleapis.com/css2?family=Oswald:wght@200;300;400;500;600;700&display=swap">
<style>
  :root {
    --ink-white: #ffffff;
    --accent-amber: #f6a918;
    --night-slate: #1d2226;
    --storm-grey: #2e3438;
    --ember-orange: #d9661c;
    --glow-gold: #f3a040;
    --paper: #ffffff;
    --label-dark: #111111;
  }
  html, body {
    margin: 0;
    padding: 0;
    width: 1200px;
    height: 900px;
    overflow: hidden;
    background: var(--night-slate);
  }
  .cover {
    position: relative;
    width: 1200px;
    height: 900px;
    overflow: hidden;
    font-family: "Oswald", "Arial Narrow", sans-serif;
    color: var(--ink-white);
  }
  .cover-photo {
    position: absolute;
    inset: 0;
    background:
      radial-gradient(ellipse 260px 200px at 905px 330px, rgba(255, 196, 110, 0.95), rgba(240, 130, 40, 0.55) 45%, rgba(0,0,0,0) 100%),
      radial-gradient(ellipse 520px 420px at 900px 380px, rgba(200, 90, 25, 0.75), rgba(0,0,0,0) 100%),
      radial-gradient(ellipse 420px 180px at 320px 610px, rgba(190, 95, 30, 0.45), rgba(0,0,0,0) 100%),
      linear-gradient(180deg, #2a3034 0%, #23282b 40%, #2b2420 70%, #160f0c 100%);
  }

  /* Back cover */
  .back-title {
    position: absolute;
    left: 150px;
    top: 44px;
    width: 280px;
    margin: 0;
    text-align: center;
    font-weight: 600;
    text-transform: uppercase;
    line-height: 0.98;
  }
  .back-title span { display: block; }
  .back-title .line-one { font-size: 40px; }
  .back-title .line-two { font-size: 44px; color: var(--accent-amber); }
  .back-title .line-three { font-size: 40px; }
  .divider {
    position: absolute;
    left: 222px;
    width: 136px;
    height: 1.5px;
    background: var(--ink-white);
  }
  .divider-top { top: 193px; }
  .divider-bottom { top: 520px; }
  .blurb {
    position: absolute;
    left: 42px;
    top: 241px;
    width: 500px;
    font-weight: 300;
    font-size: 15.5px;
    line-height: 20px;
  }
  .blurb p, .bio p { margin: 0 0 20px; }
  .blurb .title-ref { font-weight: 600; font-style: italic; }
  .blurb .title-ref em { color: var(--accent-amber); }
  .author-photo {
    position: absolute;
    left: 47px;
    top: 539px;
    width: 125px;
    height: 144px;
    background: var(--paper);
    color: var(--label-dark);
    display: flex;
    align-items: center;
    justify-content: center;
    font-size: 12.5px;
    font-weight: 500;
  }
  .bio {
    position: absolute;
    left: 188px;
    top: 541px;
    width: 345px;
    font-weight: 300;
    font-size: 15.5px;
    line-height: 20px;
  }
  .bio .author-ref { font-weight: 600; color: var(--accent-amber); }
  .barcode-area {
    position: absolute;
    left: 355px;
    top: 730px;
    width: 200px;
    height: 120px;
    background: var(--paper);
  }

  /* Spine */
  .spine-title, .spine-author {
    position: absolute;
    left: 584px;
    writing-mode: vertical-rl;
    margin: 0;
    text-transform: uppercase;
    white-space: nowrap;
  }
  .spine-title {
    top: 42px;
    font-size: 22px;
    font-weight: 600;
    letter-spacing: 0;
  }
  .spine-title em { font-style: normal; color: var(--accent-amber); }
  .spine-author {
    top: 672px;
    font-size: 22px;
    font-weight: 200;
    letter-spacing: 6px;
  }

  /* Front cover */
  .front-title {
    position: absolute;
    left: 700px;
    top: 388px;
    width: 420px;
    height: 300px;
  }
  .front-title text {
    font-family: "Oswald", "Arial Narrow", sans-serif;
    font-weight: 600;
    fill: var(--ink-white);
  }
  .subtitle {
    position: absolute;
    left: 720px;
    top: 700px;
    width: 380px;
    margin: 0;
    text-align: center;
    font-size: 19px;
    line-height: 23px;
    font-weight: 400;
    font-style: italic;
    text-transform: uppercase;
    color: var(--accent-amber);
    transform: skewX(-6deg);
  }
  .front-author {
    position: absolute;
    left: 720px;
    top: 814px;
    width: 380px;
    margin: 0;
    text-align: center;
    font-size: 32px;
    font-weight: 200;
    letter-spacing: 9px;
    text-transform: uppercase;
  }
</style>
</head>
<body>
<main class="cover">
  <div class="cover-photo" role="img" aria-label="Wraparound photograph: a runner's legs and shoes striding along a wet road at sunset, rain streaking through an orange glow, trees and a utility pole on the horizon, reflections sparkling on the asphalt"></div>

  <section class="back-cover">
    <h2 class="back-title">
      <span class="line-one">Pavement</span>
      <span class="line-two">Endurance</span>
      <span class="line-three">Blueprint</span>
    </h2>
    <div class="divider divider-top"></div>

    <div class="blurb">
      <p><span class="title-ref">Pavement <em>Endurance</em> Blueprint</span> sit amet, consectetur adipisicing elit, sed do eiusmod tempor incididunt ut labore et dolore magna aliqua. Ut enim ad minim veniam, quis nostrud exercitation ullamco laboris nisi ut aliquip ex ea commodo consequat.</p>
      <p>Duis aute irure dolor in reprehenderit in voluptate velit esse cillum dolore eu fugiat nulla pariatur. Excepteur sint occaecat cupidatat non proident, sunt in culpa qui officia deserunt mollit anim id est laborum.</p>
      <p>Sed ut perspiciatis unde omnis iste natus error sit voluptatem accusantium doloremque laudantium, totam rem aperiam, eaque ipsa quae ab illo inventore veritatis et quasi architecto beatae vitae dicta sunt explicabo. Nemo enim ipsam voluptatem quia voluptas sit aspernatur aut odit aut fugit, sed quia consequuntur magni dolores eos qui ratione voluptatem sequi nesciunt.</p>
    </div>

    <div class="divider divider-bottom"></div>

    <div class="author-photo">AUTHOR PICTURE</div>
    <div class="bio">
      <p><span class="author-ref">Author Name</span> irure dolor in reprehenderit in voluptate velit esse cillum dolore eu fugiat nulla pariatur. Excepteur sint occaecat cupidatat non proident, sunt in culpa qui officia deserunt mollit anim id est laborum.</p>
      <p>Duis aute irure dolor in reprehenderit in voluptate velit esse cillum dolore eu fugiat nulla pariatur.</p>
    </div>

    <div class="barcode-area"></div>
  </section>

  <section class="spine">
    <p class="spine-title">Pavement <em>Endurance</em> Blueprint</p>
    <p class="spine-author">Author Name</p>
  </section>

  <section class="front-cover">
    <svg class="front-title" viewBox="0 0 420 300" role="heading" aria-level="1" aria-label="Pavement Endurance Blueprint">
      <text x="3" y="88" font-size="112" textLength="414" lengthAdjust="spacingAndGlyphs">PAVEMENT</text>
      <text x="3" y="200" font-size="122" textLength="414" lengthAdjust="spacingAndGlyphs">ENDURANCE</text>
      <text x="8" y="290" font-size="100" textLength="400" lengthAdjust="spacingAndGlyphs">BLUEPRINT</text>
    </svg>
    <p class="subtitle">The Complete Handbook for Racing Your Longest Distance - Featuring Schedules, Wisdom and Target-Reaching Pointers</p>
    <p class="front-author">Author Name</p>
  </section>
</main>
</body>
</html>
```